Menu sign design for Italian Deli

Need designs for 2 hanging signs - one sided, full color, full bleed.
One sign finishes at 48" wide by 36" high, the other sign finishes at 24" wide by 36" high. (Copy and Specs included in PDF).

All files to be completed in PDF format, CMYK

Fonts, layout, colors, backgrounds, photos are totally up to you. Once we see some concepts we can give you more direction/ideas.
These signs will be used in an Italian Deli....(maybe pick-up the Italian colors?????)

```html
<!DOCTYPE html>
<html lang="en">
<head>
<meta charset="utf-8">
<title>Rocco's Deli Menu Sign</title>
<link href="https://fonts.googleapis.com/css2?family=Lobster&family=Bowlby+One&family=Merriweather:wght@400;700&family=Oswald:wght@700&display=swap" rel="stylesheet">
<style>
  :root{
    --red:#d7262f;
    --green:#1f9a4b;
    --black:#111111;
    --white:#ffffff;
    --paper:#fbfdf9;
    --tomato:#e2412c;
  }
  *{margin:0;padding:0;box-sizing:border-box;}
  html,body{width:800px;height:1200px;overflow:hidden;background:var(--white);}
  .menu-sign{position:relative;width:800px;height:1200px;overflow:hidden;background:var(--paper);font-family:'Merriweather',serif;}

  .photo{position:absolute;left:0;width:800px;}
  .photo-top{top:0;height:140px;background:linear-gradient(180deg,var(--red) 0 14px,#f4f4f0 14px 24px,var(--green) 24px 34px,#eef4e6 34px,#c9e0a8 70%,#e9efe2);}
  .photo-bottom{top:940px;height:260px;background:radial-gradient(ellipse at 55% 70%,#e04a32 0 10%,#8cc05a 24%,#cfe3b4 52%,#f4f6f1 80%);}

  .menu-panel{position:absolute;left:22px;width:756px;background:var(--white);border:5px solid var(--red);border-radius:14px;box-shadow:0 0 0 3px var(--white),0 0 0 5px var(--green);}
  .panel-salads{top:124px;height:404px;}
  .panel-platter{top:542px;height:200px;}
  .panel-fish{top:756px;height:176px;}

  .panel-title{position:absolute;left:0;right:0;top:4px;text-align:center;white-space:nowrap;line-height:72px;}
  .title-script{font-family:'Lobster',cursive;color:var(--green);font-size:58px;}
  .title-block{font-family:'Bowlby One',sans-serif;font-size:44px;letter-spacing:1px;}
  .red{color:var(--red);} .green{color:var(--green);}

  .size-badge{position:absolute;left:28px;background:var(--green);color:var(--white);font-family:'Oswald',sans-serif;font-size:26px;letter-spacing:1px;padding:10px 18px;transform:rotate(-8deg);border:3px solid var(--white);box-shadow:0 0 0 3px var(--green);}

  .price-row{position:absolute;left:220px;width:370px;height:56px;display:flex;align-items:center;}
  .size-label{font-family:'Lobster',cursive;color:var(--red);font-size:40px;width:110px;}
  .leader{flex:1;border-bottom:4px dotted var(--green);margin:0 10px 8px 0;height:0;}
  .price-pill{background:var(--green);color:var(--white);font-family:'Oswald',sans-serif;font-size:34px;border-radius:30px;padding:2px 22px;border:3px solid var(--white);box-shadow:0 0 0 3px var(--green);}
  .price-pill.is-red{background:var(--red);box-shadow:0 0 0 3px var(--red);}

  .garnish{position:absolute;width:110px;height:90px;border-radius:50%;background:radial-gradient(circle at 40% 45%,var(--tomato) 0 35%,#f07a5e 50%,#d9e9c6 72%,transparent 74%);}

  .dish-copy{position:absolute;left:40px;width:440px;font-size:16px;line-height:1.5;color:var(--black);}
  .dish-copy em{font-style:normal;color:var(--red);font-weight:700;}

  .fridays-burst{position:absolute;width:130px;height:100px;}
  .fridays-burst span{position:absolute;inset:0;display:flex;align-items:center;justify-content:center;text-align:center;font-family:'Oswald',sans-serif;font-size:20px;line-height:1;transform:rotate(-10deg);}
</style>
</head>
<body>
<main class="menu-sign">
  <div class="photo photo-top" role="img" aria-label="Fresh garden salad with tomatoes and greens under a red, white and green pennant strip"></div>

  <section class="menu-panel panel-salads">
    <h2 class="panel-title"><span class="title-script">Fresh </span><span class="title-block red">GARDEN </span><span class="title-block green">SALADS</span></h2>

    <div class="size-badge" style="top:118px;">PLAIN</div>
    <div class="size-badge" style="top:270px;">SPECIALTY</div>

    <div class="price-row" style="top:92px;"><span class="size-label">Small</span><span class="leader"></span><span class="price-pill">$2.99</span></div>
    <div class="price-row" style="top:162px;"><span class="size-label">Large</span><span class="leader"></span><span class="price-pill">$4.99</span></div>
    <div class="price-row" style="top:248px;"><span class="size-label">Small</span><span class="leader"></span><span class="price-pill">$4.99</span></div>
    <div class="price-row" style="top:318px;"><span class="size-label">Large</span><span class="leader"></span><span class="price-pill">$7.99</span></div>

    <div class="garnish" style="left:620px;top:112px;" role="img" aria-label="Cherry tomatoes on the vine with garlic"></div>
    <div class="garnish" style="left:620px;top:268px;" role="img" aria-label="Cherry tomatoes on the vine with garlic"></div>
  </section>

  <section class="menu-panel panel-platter">
    <h2 class="panel-title"><span class="title-script">Rocco's </span><span class="title-block red">GARBAGE </span><span class="title-block green">PLATTER</span></h2>
    <p class="dish-copy" style="top:86px;">Your choice of <em>2 Hamburgs</em>, <em>Cheeseburgs</em>, <em>Hot Dogs</em> or <em>Italian Sausages</em>. With <em>Fries</em> and <em>Mac</em> or <em>Potato Salad</em>, top with <em>Onions</em>, <em>Meat Hot Sauce</em>, <em>Ketchup</em>, or <em>Mustard</em>.</p>
    <div class="price-row" style="top:104px;left:492px;width:auto;"><span class="price-pill is-red">$9.99</span></div>
    <div class="garnish" style="left:624px;top:88px;" role="img" aria-label="Cherry tomatoes on the vine with garlic"></div>
  </section>

  <section class="menu-panel panel-fish">
    <h2 class="panel-title"><span class="title-script">Haddock </span><span class="title-block red">FISH </span><span class="title-block green">FRY</span></h2>
    <p class="dish-copy" style="top:86px;">Your choice of <em>Beer Battered</em>, <em>Breaded</em>, or <em>Broiled</em> with <em>Potato Wedges</em>, <em>Coleslaw</em>, <em>Lemon</em>, <em>Salt</em>, <em>Pepper</em>, <em>Butter</em>, <em>Ketchup</em>, and a <em>roll</em>.</p>
    <div class="price-row" style="top:92px;left:492px;width:auto;"><span class="price-pill">$9.99</span></div>
    <div class="garnish" style="left:624px;top:78px;width:104px;height:84px;" role="img" aria-label="Cherry tomatoes on the vine with garlic"></div>
  </section>

  <div class="fridays-burst" style="left:6px;top:740px;">
    <svg viewBox="0 0 120 120" width="130" height="100" preserveAspectRatio="none" aria-hidden="true"><polygon fill="var(--black)" points="118,60 105.1,69 113.6,82.2 98.2,85.6 101,101 85.6,98.2 82.2,113.6 69,105.1 60,118 51,105.1 37.8,113.6 34.4,98.2 19,101 21.8,85.6 6.4,82.2 14.9,69 2,60 14.9,51 6.4,37.8 21.8,34.4 19,19 34.4,21.8 37.8,6.4 51,14.9 60,2 69,14.9 82.2,6.4 85.6,21.8 101,19 98.2,34.4 113.6,37.8 105.1,51"/></svg>
    <span style="color:var(--red);">FRIDAYS<br>ONLY</span>
  </div>
  <div class="fridays-burst" style="left:664px;top:740px;">
    <svg viewBox="0 0 120 120" width="130" height="100" preserveAspectRatio="none" aria-hidden="true"><polygon fill="var(--red)" points="118,60 105.1,69 113.6,82.2 98.2,85.6 101,101 85.6,98.2 82.2,113.6 69,105.1 60,118 51,105.1 37.8,113.6 34.4,98.2 19,101 21.8,85.6 6.4,82.2 14.9,69 2,60 14.9,51 6.4,37.8 21.8,34.4 19,19 34.4,21.8 37.8,6.4 51,14.9 60,2 69,14.9 82.2,6.4 85.6,21.8 101,19 98.2,34.4 113.6,37.8 105.1,51"/></svg>
    <span style="color:var(--black);">FRIDAYS<br>ONLY</span>
  </div>

  <div class="photo photo-bottom" role="img" aria-label="Bowl of mixed garden salad with tomatoes, olives and a fork"></div>
</main>
</body>
</html>
```